Company or website name
- Jardin Lumineux
- Slogan or Tagline
- No Taglines, but each description listed here needs to be on the front label of each of these wines.
- Describe your company and organization and target audience
- Consumers buying wine aged 30+, restaurants. Of wine buyers, 55% are female shopping at major grocery chains.
- The design should have the following
- The style should marry traditional sophistication with a touch of contemporary fun. It should tell knowledgeable wine buyers that it is a serious, quality product, but have enough light to attract the novice wine buyers and impulse buyers. Must have: 1) Jardin Lumineux (brand name) 2) Method Traditionelle 3) Appellation Cremant de Limoux Controlee 4) Product of France -Brut -Brut RoseFountaine de la Vie means "Bright Garden" in French We would like this idea implemented into the design of the label. As a sparkling wine, bubbles are what spring from this fountain.
- This design should not have this in the entries
- No use of Gold or Gold Foil (scratches too easily). Also, black labels tend to scuff and don't travel well (plus they don't stand out on the shelves as much). Not too frilly – this is a quality product. We do not want to turn off serious wine buyers because they don’t take the label seriously.

```html
<!DOCTYPE html>
<html lang="en">
<head>
<meta charset="utf-8">
<title>Jardin Lumineux – Brut Label</title>
<link rel="stylesheet" href="https://fonts.googleapis.com/css2?family=Cabin:wght@400;500&family=Dancing+Script:wght@600&display=swap">
<style>
  :root {
    --page: #ffffff;
    --rim-green: #34a843;
    --rim-yellow: #e3e82c;
    --fill-left: #a9d437;
    --fill-mid: #d3e22a;
    --fill-right: #3db54a;
    --ink: #3a9d3b;
    --ink-deep: #2b8d39;
    --ornament: #e6ec3a;
    --ornament-low: #2f9a3e;
  }
  html, body {
    margin: 0;
    padding: 0;
    width: 1200px;
    height: 958px;
    overflow: hidden;
    background: var(--page);
  }
  .label {
    position: relative;
    width: 1200px;
    height: 958px;
  }
  .label-shape {
    position: absolute;
    inset: 0;
  }
  .ornament {
    position: absolute;
    border-radius: 50%;
  }
  .ornament--top {
    left: 435px; top: 100px; width: 330px; height: 76px;
    background: radial-gradient(ellipse at center, var(--ornament) 0%, rgba(230,236,58,0.55) 55%, rgba(230,236,58,0) 75%);
  }
  .ornament--bottom {
    left: 477px; top: 802px; width: 246px; height: 54px;
    background: radial-gradient(ellipse at center, var(--ornament-low) 0%, rgba(47,154,62,0.5) 55%, rgba(47,154,62,0) 75%);
  }
  .style-name,
  .appellation,
  .method,
  .origin {
    position: absolute;
    left: 0;
    width: 1200px;
    text-align: center;
    font-family: "Cabin", sans-serif;
    color: var(--ink);
    margin: 0;
  }
  .style-name {
    top: 204px;
    font-size: 28px;
    font-weight: 500;
    letter-spacing: 1px;
  }
  .brand {
    position: absolute;
    left: 0;
    width: 1200px;
    top: 290px;
    margin: 0;
    font-family: "Dancing Script", cursive;
    font-weight: 600;
    color: var(--ink-deep);
    text-align: center;
    line-height: 1;
  }
  .brand-line {
    display: block;
  }
  .brand-line--first {
    font-size: 138px;
    margin-left: -40px;
  }
  .brand-line--second {
    font-size: 112px;
    margin-top: 4px;
    margin-left: 90px;
  }
  .appellation {
    top: 614px;
    font-size: 33px;
    font-weight: 400;
  }
  .rule {
    position: absolute;
    left: 393px;
    top: 661px;
    width: 417px;
    height: 2px;
    background: linear-gradient(90deg, rgba(58,157,59,0.2), var(--ink) 25%, var(--ink) 75%, rgba(58,157,59,0.2));
  }
  .method {
    top: 674px;
    font-size: 15px;
    font-weight: 500;
    letter-spacing: 2px;
  }
  .origin {
    top: 756px;
    font-size: 23px;
    font-weight: 400;
  }
</style>
</head>
<body>
  <main class="label">
    <svg class="label-shape" width="1200" height="958" viewBox="0 0 1200 958" aria-hidden="true">
      <defs>
        <linearGradient id="label-fill" x1="0" y1="0" x2="1" y2="0">
          <stop offset="0" stop-color="var(--fill-left)"/>
          <stop offset="0.45" stop-color="var(--fill-mid)"/>
          <stop offset="1" stop-color="var(--fill-right)"/>
        </linearGradient>
      </defs>
      <ellipse class="rim-outer" cx="600" cy="478" rx="341" ry="459" fill="var(--rim-green)"/>
      <ellipse class="rim-inner" cx="600" cy="478" rx="330" ry="448" fill="var(--rim-yellow)"/>
      <ellipse class="label-field" cx="600" cy="478" rx="321" ry="439" fill="url(#label-fill)"/>
    </svg>

    <div class="ornament ornament--top" role="img" aria-label="Decorative flourish ornament"></div>

    <p class="style-name">BRUT</p>

    <h1 class="brand">
      <span class="brand-line brand-line--first">Jardin</span>
      <span class="brand-line brand-line--second">Lumineux</span>
    </h1>

    <p class="appellation">Cremant de Limoux</p>
    <div class="rule"></div>
    <p class="method">METHOD TRADITIONELLE</p>

    <p class="origin">Product of France</p>

    <div class="ornament ornament--bottom" role="img" aria-label="Decorative flourish ornament"></div>
  </main>
</body>
</html>
```